Business Card Design

Buy and sell properties
Buy and rehab properties
Buy properties for cash
That is what I do but do need a logo
looking for some type of logo or design on it
Just started business
Back of card should say something like BUY HOUSES CASH
Overview: it is a new company. Basically I buy properties wholesale and fix them up and sell them or sell them to other fix and flippers
Background: company is new so not any background
Market: is basically anyone selling a house or buying a house. Someone that needs to sell house fast. Basically I am a cash home buyer!!!

Email on card should be:   harborvalepropertiesinc@example-mail.com

Industry/Entity Type
House
Contact Information for Business Card
Harbor Vale Properties Inc
PO Box 718264
Coral Marsh FL 34197

Dale Morcott
dmorcott@example-mail.com
555-271-9083

```html
<!DOCTYPE html>
<html lang="en">
<head>
<meta charset="utf-8">
<title>Harbor Vale Properties Inc – Business Cards</title>
<link href="https://fonts.googleapis.com/css2?family=Questrial&family=Open+Sans:wght@400;600;700&display=swap" rel="stylesheet">
<style>
  :root {
    --stage: #2a2c2f;
    --paper: #ffffff;
    --ink: #3b3c3e;
    --blue: #1f5fae;
    --blue-deep: #123f8f;
    --blue-light: #3a86cf;
    --green: #2f9a3c;
    --white: #ffffff;
  }
  * { box-sizing: border-box; margin: 0; padding: 0; }
  html, body { width: 1200px; height: 790px; overflow: hidden; }
  body {
    background: var(--stage);
    position: relative;
    font-family: "Open Sans", Arial, sans-serif;
  }

  .card {
    position: absolute;
    background: var(--paper);
    overflow: hidden;
  }

  /* Brand wordmark: one colour, one weight */
  .wordmark {
    display: flex;
    align-items: center;
    gap: 14px;
    font-family: "Questrial", Arial, sans-serif;
    color: var(--ink);
    font-weight: 400;
    white-space: nowrap;
  }
  .wordmark-square {
    flex: none;
    background: var(--blue);
  }

  /* Back of card */
  .card-back { left: 310px; top: 48px; width: 600px; height: 280px; }
  .card-back .wordmark {
    position: absolute; left: 0; right: 0; top: 108px;
    justify-content: center; font-size: 34px;
  }
  .card-back .wordmark-square { width: 30px; height: 30px; }
  .slogan-band {
    position: absolute; left: 0; right: 0; bottom: 0; height: 34px;
    background: linear-gradient(90deg, var(--blue-deep), var(--blue-light) 50%, var(--blue-deep));
    display: flex; align-items: center; justify-content: center; gap: 12px;
  }
  .slogan-rule { width: 170px; height: 1px; background: rgba(255,255,255,.75); }
  .slogan {
    color: var(--white); font-weight: 700; font-size: 15px; letter-spacing: .5px;
  }

  /* Front of card */
  .card-front { left: 490px; top: 378px; width: 660px; height: 330px; }
  .card-front .wave { position: absolute; inset: 0; width: 100%; height: 100%; }
  .card-front .wordmark {
    position: absolute; left: 46px; top: 48px; font-size: 26px;
  }
  .card-front .wordmark-square { width: 22px; height: 22px; }
  .contact {
    position: absolute; right: 28px; top: 150px;
    text-align: right; color: var(--white); font-size: 13px; line-height: 20px;
    white-space: nowrap;
  }
  .contact-line { display: flex; justify-content: flex-end; align-items: center; gap: 7px; }
  .contact-icon { width: 12px; height: 12px; fill: var(--white); }
  .contact-company { font-weight: 700; }
  .holder-name {
    position: absolute; left: 44px; bottom: 40px;
    color: var(--white); font-weight: 700; font-size: 25px;
  }

  /* Logo sheet */
  .logo-sheet {
    position: absolute; left: 8px; top: 510px; width: 420px; height: 270px;
    background: var(--paper);
    display: flex; align-items: center; justify-content: center;
  }
  .logo-sheet .wordmark { font-size: 28px; }
  .logo-sheet .wordmark-square { width: 26px; height: 26px; }
</style>
</head>
<body>

  <section class="card card-back" aria-label="Back of business card">
    <div class="wordmark">
      <span class="wordmark-square"></span>
      <span>Harbor Vale Properties Inc</span>
    </div>
    <div class="slogan-band">
      <span class="slogan-rule"></span>
      <span class="slogan">BUY HOUSES CASH</span>
      <span class="slogan-rule"></span>
    </div>
  </section>

  <section class="card card-front" aria-label="Front of business card">
    <svg class="wave" viewBox="0 0 660 330" preserveAspectRatio="none" aria-hidden="true">
      <defs>
        <radialGradient id="blueField" cx="70%" cy="60%" r="70%">
          <stop offset="0" stop-color="#2f74c4"/>
          <stop offset="1" stop-color="#123f8f"/>
        </radialGradient>
      </defs>
      <path d="M0 193 C150 203 260 188 340 128 C420 68 540 33 660 28 L660 40 C540 45 420 80 340 140 C260 200 150 215 0 205 Z" fill="#2f9a3c"/>
      <path d="M0 205 C150 215 260 200 340 140 C420 80 540 45 660 40 L660 330 L0 330 Z" fill="url(#blueField)"/>
    </svg>
    <div class="wordmark">
      <span class="wordmark-square"></span>
      <span>Harbor Vale Properties Inc</span>
    </div>
    <div class="contact">
      <div class="contact-line">555-271-9083
        <svg class="contact-icon" viewBox="0 0 16 16" aria-hidden="true"><path d="M3 1h3l1.5 4-2 1.3a9 9 0 0 0 4.2 4.2L11 8.5l4 1.5v3a2 2 0 0 1-2 2A12 12 0 0 1 1 3a2 2 0 0 1 2-2z"/></svg>
      </div>
      <div class="contact-line">harborvalepropertiesinc@example-mail.com
        <svg class="contact-icon" viewBox="0 0 16 16" aria-hidden="true"><path d="M1 3h14v10H1z M2 4l6 5 6-5" fill="none" stroke="#fff" stroke-width="1.5"/></svg>
      </div>
      <div class="contact-company">Harbor Vale Properties Inc</div>
      <div>PO Box 718264</div>
      <div>Coral Marsh FL 34197</div>
    </div>
    <div class="holder-name">Dale Morcott</div>
  </section>

  <section class="logo-sheet" aria-label="Logo sheet">
    <div class="wordmark">
      <span class="wordmark-square"></span>
      <span>Harbor Vale Properties Inc</span>
    </div>
  </section>

</body>
</html>
```